ProLattice background/title banner

Feel free to visit my website (kvohomecheck.ca) and current NetLoop (KVO Property Inspections) page for a general feel. We focus on our trades background and experience. I have uploaded some logos that I would like used here. We offer Commercial, Residential, Agricultural inspections. With 24/7 online booking and call center.
Updates
Please ensure the small logos are added. Try to use all 3 colors. Red, Grey, Black (and some white), leave room for the profile pic that appear in the bottom left as well.
Target Market(s)
realtors and real estate professionals
Industry/Entity Type
Property Inspections for Real Estate
Logo Text
"Inspected by Tradesmen"
Font styles to use
Requirements
Must have
- To be simple with the key highlights and logos.

```html
<!DOCTYPE html>
<html lang="en">
<head>
<meta charset="utf-8">
<title>Property Inspections Banner</title>
<link href="https://fonts.googleapis.com/css2?family=Raleway:wght@500;600&family=Montserrat:wght@600&display=swap" rel="stylesheet">
<style>
  :root {
    --brand-red: #e8401f;
    --brand-red-light: #f06a4c;
    --band-grey: #3b3b3b;
    --paper: #ffffff;
    --badge-orange: #f2862a;
    --badge-red: #d9262b;
    --badge-blue: #3d9ad6;
    --badge-navy: #1f4e8c;
    --badge-black: #1a1a1a;
  }
  * { margin: 0; padding: 0; box-sizing: border-box; }
  html, body { width: 1200px; height: 203px; overflow: hidden; background: var(--paper); }
  .banner { position: relative; width: 1200px; height: 203px; background: var(--paper); }
  .hero-band { position: absolute; left: 0; top: 0; width: 1200px; height: 113px; background: var(--brand-red); }
  .divider-band { position: absolute; left: 0; top: 113px; width: 1200px; height: 9px; background: var(--band-grey); }
  .roof-mark {
    position: absolute; left: 38px; top: 5px; width: 356px; height: 108px;
    background: linear-gradient(180deg, var(--brand-red-light), var(--brand-red));
  }
  .headline { position: absolute; left: 427px; top: 35px; color: var(--paper); font-family: 'Raleway', sans-serif; }
  .headline-sub { display: block; font-size: 21px; font-weight: 600; letter-spacing: 0.2px; line-height: 23px; }
  .headline-main { display: block; font-size: 45.5px; font-weight: 600; letter-spacing: 0.5px; line-height: 44px; }
  .services {
    position: absolute; left: 780px; top: 15px; list-style: none;
    color: var(--paper); font-family: 'Montserrat', sans-serif; font-size: 10.4px; font-weight: 600; line-height: 14px;
  }
  .services li { white-space: nowrap; }
  .services li::before { content: "\2022"; margin-right: 4px; }
  .partner-badges { position: absolute; left: 747px; top: 139px; width: 250px; height: 49px; }
</style>
</head>
<body>
<div class="banner">
  <div class="hero-band"></div>
  <div class="divider-band"></div>
  <div class="roof-mark" role="img" aria-label="White roofline with chimney and four-pane window, the company's house logo mark"></div>

  <h1 class="headline">
    <span class="headline-sub">RESIDENTIAL &amp; COMMERCIAL</span>
    <span class="headline-main">INSPECTIONS</span>
  </h1>

  <ul class="services">
    <li>Property Inspections</li>
    <li>Mold &amp; Asbestos Testing</li>
    <li>Acreage Inspections</li>
    <li>Pre-purchase Inspections</li>
    <li>Ozone/Odor Treatment</li>
    <li>Woodstove Inspections</li>
    <li>And More...</li>
  </ul>

  <svg class="partner-badges" viewBox="0 0 250 49" aria-label="Partner and certification badges">
    <rect x="0" y="1" width="28" height="45" rx="4" fill="var(--badge-orange)"/>
    <circle cx="57" cy="24" r="22" fill="var(--badge-red)"/>
    <circle cx="108" cy="24" r="22" fill="var(--badge-blue)"/>
    <rect x="139" y="16" width="54" height="16" rx="2" fill="var(--badge-navy)"/>
    <rect x="200" y="2" width="50" height="45" rx="3" fill="var(--badge-black)"/>
  </svg>
</div>
</body>
</html>
```